Modern, Clean website for painting service.

We are working with a company called Brush Harbor and building a new website for them.

Some sites to use for content/competitors and inspiration:

https://www.coatwellcrew.example
https://ridgeline-coats.example
https://tevinhallorpainting.example

Thank you for taking the time to consider designing a website for us. We are web developers based in Stockton, CA, USA. Most of our projects go through the same process. Understanding this process may help you win a project with us. We custom-code all of our websites in-house. We don’t have any requirements as to what tools you use for your design, but we prefer Figma files. For any design that we label as four-stars, we send it to the client for review. The client picks the final design they want us to use. Once we complete this process, we will continue to show additional clients all the four-star sites and purchase them later. Your designs will have multiple chances to sell. For better chances of success, we ask that you follow these guidelines.

IMAGES:
If you use any images or icons in the design, we ask that you have a link to the asset so we can purchase the image/icon. Most of the designs we submit do not have the customer’s images on them unless they have some great images. Be creative; show us the feeling you are trying to portray with your image choices. Use any royalty-free site you choose. We subscribe to Adobe and mainly use their images, but we can purchase images outside of Adobe. PLEASE NOTE: we will not submit designs to clients with watermarks on the images.

FONTS:
We ask that you identify the fonts used in the design. This can be done in a message if you want. We typically use Google Fonts and Adobe Fonts.

CONTENT:
We're always open to different content and ideas. We often submit designs with stock images so the client can see our vision. We typically take pictures after the website launch to use their images with our vision. Lorem Ipsum is fine for paragraphs, but we ask that you write the headers in correct English. We want to be able to show the vision and identify the sections of the website.

INSPIRATION:
We typically add a couple of links in the brief of websites we like to help you get started in your design.

REVISIONS:
We do not often ask for revisions of the designs unless we see something in the design that may not appeal to the client. If there are slight changes that we want to make, we do that in the development process.

FEEDBACK:
We rarely give feedback on designs during the design process. We are working on many website projects and do not have the time to provide feedback. We usually respond if your request is well thought out and asks specific questions, but a note asking “feedback, please” usually goes unanswered.

```html
<!DOCTYPE html>
<html lang="en">
<head>
<meta charset="utf-8">
<title>Brush Harbor – House Painting Services</title>
<link href="https://fonts.googleapis.com/css2?family=Jost:wght@400;500;600&family=Poppins:wght@400;500&display=swap" rel="stylesheet">
<style>
:root{
  --navy:#1b2452;
  --navy-deep:#16204a;
  --crimson:#8c0a24;
  --rose:#c22a4d;
  --ink:#111;
  --body:#444;
  --muted:#8a8a8a;
  --paper:#f7f7f7;
  --white:#fff;
  --green:#3fae4a;
  --blue:#2a7fd0;
}
*{margin:0;padding:0;box-sizing:border-box}
html,body{width:1200px;height:4245px;overflow:hidden}
body{position:relative;background:var(--paper);font-family:"Poppins",sans-serif;color:var(--ink)}
.abs{position:absolute}
h1,h2,h3,h4{font-family:"Jost",sans-serif;font-weight:500}

/* header */
.site-header{left:0;top:0;width:1200px;height:94px;background:var(--white)}
.brand{display:flex;align-items:center;gap:10px}
.brand-mark{width:22px;height:22px;background:var(--crimson)}
.brand-name{font-family:"Jost",sans-serif;font-weight:500;font-size:22px;letter-spacing:2px;color:var(--navy);white-space:nowrap}
.header-brand{left:38px;top:34px}
.header-phone{left:730px;top:32px;display:flex;align-items:center;gap:8px;font-family:"Jost",sans-serif;font-size:23px;font-weight:500;color:var(--ink);white-space:nowrap}
.btn{display:flex;align-items:center;justify-content:center;font-family:"Jost",sans-serif;color:var(--white);letter-spacing:3px;text-transform:uppercase;white-space:nowrap}
.btn-navy{background:var(--navy)}
.btn-grad{background:linear-gradient(90deg,var(--navy),var(--crimson))}
.header-contact{left:997px;top:28px;width:150px;height:42px;font-size:15px}

.main-nav{left:0;top:94px;width:1200px;height:51px;background:linear-gradient(90deg,var(--navy) 0%,#3a2250 50%,var(--crimson) 100%);display:flex;align-items:center}
.main-nav a{position:absolute;color:var(--white);text-decoration:none;font-family:"Jost",sans-serif;font-size:19px;letter-spacing:4px}

/* hero */
.hero{left:0;top:145px;width:1200px;height:613px;background:linear-gradient(90deg,rgba(40,45,95,.95) 0%,rgba(120,40,85,.85) 45%,rgba(190,40,75,.9) 100%)}
.hero-figure{left:520px;top:160px;width:640px;height:600px;background:radial-gradient(ellipse at 60% 45%,rgba(235,190,190,.35),rgba(60,80,160,.25) 60%,transparent 75%)}
.hero-title{left:30px;top:250px;font-size:72px;line-height:86px;color:var(--white);font-weight:500;letter-spacing:1px}
.hero-text{left:30px;top:436px;width:500px;font-size:16px;line-height:22px;color:var(--white)}
.hero-btn{left:30px;top:528px;width:192px;height:37px;font-size:14px}

.feature{width:275px;height:172px;background:var(--white);top:680px;display:flex;flex-direction:column;align-items:center;justify-content:flex-start;padding-top:18px}
.feature::after{content:"";position:absolute;left:-4px;right:-4px;bottom:-4px;height:4px;background:linear-gradient(90deg,var(--navy),var(--crimson))}
.feature svg{width:76px;height:82px}
.feature h3{font-size:27px;margin-top:6px;color:var(--ink)}

/* offer */
.offer-title{left:67px;top:1002px;font-size:36px;line-height:44px;font-weight:500;color:var(--ink)}
.offer-text{left:67px;top:1150px;width:490px;font-size:13.5px;line-height:26px;color:var(--body)}
.offer-btn{left:67px;top:1303px;width:150px;height:44px;font-size:16px;letter-spacing:4px}
.photo{background:linear-gradient(135deg,#6b7690,#c9b7ad 50%,#e8d4cc)}

/* services */
.services{left:0;top:1478px;width:1200px;height:367px;background:linear-gradient(90deg,rgba(35,50,110,1) 0%,rgba(110,50,90,.95) 50%,rgba(195,40,75,1) 100%)}
.section-title{left:0;width:1200px;text-align:center;font-size:37px;font-weight:500;color:var(--ink)}
.services-title{top:1540px;color:var(--white)}
.service-card{top:1633px;width:310px;height:322px;background:var(--white)}
.service-card .photo{width:310px;height:262px}
.service-card p{height:60px;display:flex;align-items:center;justify-content:center;font-family:"Jost",sans-serif;font-size:18px;font-weight:500;letter-spacing:.5px}

/* recent work */
.work-title{top:2048px;font-size:36px;font-weight:600}
.work-grid{left:84px;top:2152px;width:1026px;height:436px;display:grid;grid-template-columns:repeat(3,1fr);grid-template-rows:repeat(2,1fr)}

/* quote */
.quote{left:0;top:2710px;width:1200px;height:590px;background:var(--white)}
.quote-title{left:117px;top:2838px;font-size:37px;font-weight:600}
.field{background:#f4f4f4;font-size:10px;color:#666;padding:8px 14px;height:28px}
.quote-btn{left:108px;top:3082px;width:458px;height:34px;background:var(--crimson);font-size:10px;letter-spacing:0;font-weight:600}
.quote-figure{left:570px;top:2820px;width:580px;height:420px;background:linear-gradient(180deg,#f4ede4,#e0eef7)}

/* blog */
.blog-title{top:3322px;font-size:36px;font-weight:600}
.blog-card{top:3430px;width:305px;height:380px}
.blog-card .photo{width:305px;height:205px}
.blog-body{position:absolute;left:33px;top:190px;width:240px;background:var(--white);padding:22px 0 0 0}
.blog-body h4{font-size:19px;line-height:25px;color:#333;font-weight:400}
.blog-body p{font-size:11px;line-height:23px;color:var(--muted);margin-top:10px}
.blog-meta{font-size:10px;color:var(--muted);border-top:1px solid #eee;margin-top:12px;padding-top:12px}
.blog-meta .cat{color:var(--green);font-weight:500}

/* footer */
.site-footer{left:0;top:3847px;width:1200px;height:398px;background:var(--navy-deep);color:var(--white)}
.footer-brand .brand-name{color:var(--white)}
.footer-brand .brand-mark{background:var(--rose)}
.footer-text{font-size:10px;line-height:14px;color:#d8dbe8;width:290px}
.footer-head{font-family:"Jost",sans-serif;font-size:19px;font-weight:400;letter-spacing:.5px}
.footer-links li{list-style:none;font-size:13px;margin-bottom:24px;display:flex;align-items:center;gap:10px}
.footer-links li::before{content:"";width:4px;height:4px;border-radius:50%;background:var(--rose)}
.contact-row{display:flex;align-items:center;gap:12px;margin-bottom:20px}
.contact-row small{display:block;font-size:8px;letter-spacing:.5px}
.contact-row span{font-size:13px;white-space:nowrap}
.dot-icon{width:20px;height:20px;border-radius:50%;background:var(--rose);display:flex;align-items:center;justify-content:center}
.email-field{left:949px;top:3995px;width:157px;height:30px;background:var(--white);color:#999;font-size:9px;display:flex;align-items:center;justify-content:center;letter-spacing:.5px}
.signup{left:949px;top:4035px;width:157px;height:30px;background:#c01a3e;font-size:12px;letter-spacing:0;font-weight:600}
.social{width:16px;height:16px;border-radius:50%;border:2px solid var(--white)}
.legal{font-size:10px;color:#e6e7ef;white-space:nowrap}
</style>
</head>
<body>

<header class="abs site-header">
  <div class="abs brand header-brand"><span class="brand-mark"></span><span class="brand-name">BRUSH HARBOR</span></div>
  <div class="abs header-phone">
    <svg width="30" height="30" viewBox="0 0 24 24"><path fill="#b3162f" d="M6.6 10.8a15.1 15.1 0 0 0 6.6 6.6l2.2-2.2a1 1 0 0 1 1-.25 11.4 11.4 0 0 0 3.6.57 1 1 0 0 1 1 1V20a1 1 0 0 1-1 1A17 17 0 0 1 3 4a1 1 0 0 1 1-1h3.5a1 1 0 0 1 1 1c0 1.25.2 2.45.57 3.57a1 1 0 0 1-.25 1z"/></svg>
    209-555-0148
  </div>
  <a class="abs btn btn-navy header-contact">Contact</a>
</header>

<nav class="abs main-nav">
  <a style="left:142px">HOME</a>
  <a style="left:295px">ABOUT</a>
  <a style="left:462px">SERVICES</a>
  <a style="left:665px">PORTFOLIO</a>
  <a style="left:892px;letter-spacing:0">CONTACT</a>
</nav>

<section class="abs hero" role="img" aria-label="Bright painted living room interior with a smiling painter holding a colour fan and brush"></section>
<div class="abs hero-figure" aria-hidden="true"></div>
<h1 class="abs hero-title">House Painting<br>Services</h1>
<p class="abs hero-text">Lorem ipsum dolor sit amet, consectetur adipiscing elit, sed do eiusmod temporincididunt ut labore et dolore magna aliqua. Ut enim ad minim veniam</p>
<a class="abs btn btn-navy hero-btn">Get a Quote</a>

<div class="abs feature" style="left:100px">
  <svg viewBox="0 0 76 82" fill="none" stroke="#b3162f" stroke-width="2.5"><rect x="4" y="4" width="48" height="16" rx="3"/><path d="M52 12h10v18H34v12"/><rect x="29" y="42" width="10" height="34" rx="4"/></svg>
  <h3>Quality Finish</h3>
</div>
<div class="abs feature" style="left:457px">
  <svg viewBox="0 0 76 82" fill="none" stroke="#b3162f" stroke-width="2.5"><path d="M6 40 38 10l32 30"/><path d="M14 34v40h48V34"/><rect x="30" y="50" width="16" height="24"/><rect x="20" y="40" width="10" height="10"/><rect x="46" y="40" width="10" height="10"/></svg>
  <h3>Best Support</h3>
</div>
<div class="abs feature" style="left:813px">
  <svg viewBox="0 0 76 82" fill="none" stroke="#b3162f" stroke-width="2.5"><path d="M24 20h22l18 30-24 20-22-28z"/><circle cx="38" cy="48" r="9"/><path d="M38 42v12M35 45h5a2 2 0 0 1 0 4h-4a2 2 0 0 0 0 4h5"/><path d="M34 20c0-10 10-14 14-6"/></svg>
  <h3>Better Price</h3>
</div>

<h2 class="abs offer-title">We offer Residential &amp;<br>Commercial Painting<br>services</h2>
<p class="abs offer-text">Com uma rede consolidada de escritórios e agentes em todo o mundo, na Marlow Logistics oferecemos soluções integradas de importação e exportação de acordo com as necessidades dos nossos clientes a nível nacional e internacional. Conheça todos os serviços que oferecemos para sua empresa!</p>
<a class="abs btn btn-grad offer-btn">Contact</a>
<div class="abs photo" style="left:626px;top:979px;width:496px;height:377px;background:linear-gradient(135deg,#4b5f80,#c9b0a4 45%,#e7875e 55%,#efe6e2)" role="img" aria-label="Coral paint pouring from a can onto a floor"></div>

<section class="abs services" role="img" aria-label="Freshly painted room with curtains, tinted in navy and crimson"></section>
<h2 class="abs section-title services-title">Our Quality Services</h2>
<div class="abs service-card" style="left:67px">
  <div class="photo" style="background:linear-gradient(135deg,#5f9a3c,#7fbf52 50%,#2d6fa0)" role="img" aria-label="Two workers rolling green paint on a wall"></div>
  <p>RESIDENTIAL PROJECTS</p>
</div>
<div class="abs service-card" style="left:441px">
  <div class="photo" style="background:linear-gradient(135deg,#6fa3c9,#c9d9e6 50%,#2f6d4a)" role="img" aria-label="Worker using a drill on a blue wall"></div>
  <p>COMMERCIAL PROJECTS</p>
</div>
<div class="abs service-card" style="left:816px">
  <div class="photo" style="background:linear-gradient(135deg,#cbc6bd,#8a3a22 55%,#3b1a10)" role="img" aria-label="Brush staining wooden boards"></div>
  <p>RESTORATION PROJECTS</p>
</div>

<h2 class="abs section-title work-title">RECENT WORK</h2>
<div class="abs work-grid">
  <div style="background:linear-gradient(160deg,#efe9e1,#b8a58c)" role="img" aria-label="Painted living room with fireplace"></div>
  <div style="background:linear-gradient(180deg,#2c4a8f,#1f3570)" role="img" aria-label="Blue wall behind a blue sofa"></div>
  <div style="background:linear-gradient(180deg,#e6a93a,#d6962c 70%,#efe8de)" role="img" aria-label="Mustard yellow wall with shelf and plants"></div>
  <div style="background:linear-gradient(180deg,#5b97d6,#f0efec 55%,#c2383a)" role="img" aria-label="White house with red trim"></div>
  <div style="background:linear-gradient(90deg,#ddd,#7a3b22 30%,#5a2a18)" role="img" aria-label="Stained wooden fence beside a white pillar"></div>
  <div style="background:linear-gradient(180deg,#cfe2f3,#3d63b8 50%,#e9e9e9)" role="img" aria-label="Blue painted industrial building"></div>
</div>

<section class="abs quote"></section>
<h2 class="abs quote-title">GET A QUOTE</h2>
<div class="abs field" style="left:117px;top:2922px;width:210px">Your Name</div>
<div class="abs field" style="left:358px;top:2922px;width:208px">Your Phone</div>
<div class="abs field" style="left:117px;top:2967px;width:210px">Email Address</div>
<div class="abs field" style="left:358px;top:2967px;width:208px">Select Service</div>
<div class="abs field" style="left:117px;top:3012px;width:449px;height:55px">Additional Message</div>
<a class="abs btn quote-btn">GET A FREE QUOTE NOW</a>
<div class="abs quote-figure" role="img" aria-label="Cheerful painter with a roller standing by a wooden ladder"></div>

<h2 class="abs section-title blog-title">LATEST FROM BLOG</h2>
<article class="abs blog-card" style="left:122px">
  <div class="photo" style="background:linear-gradient(135deg,#3a3a3a,#d9d9d9 60%,#f4f4f4)" role="img" aria-label="Painter in a white kitchen"></div>
  <div class="blog-body">
    <h4>Ideas For Kitchen Renovation</h4>
    <p>Painting has been the industry's standard dummy text ever since the 1500s, when an...</p>
    <div class="blog-meta"><span class="cat">Ink Paint</span> • 11 Mar 2016 • 1 Comment</div>
  </div>
</article>
<article class="abs blog-card" style="left:443px">
  <div class="photo" style="background:linear-gradient(135deg,#c9b39c,#8a4a2a 60%,#5b2e18)" role="img" aria-label="Hand brushing stain on a wooden floor"></div>
  <div class="blog-body">
    <h4>The Benefits of High-Quality Paint</h4>
    <p>Phasellus aliquet, risus at blandit lobortis, tortor neque accumsan sem, in aliquet purus purus...</p>
    <div class="blog-meta"><span class="cat" style="color:var(--blue)">Spray Paint</span> • 11 Mar 2016 • 1 Comment</div>
  </div>
</article>
<article class="abs blog-card" style="left:764px">
  <div class="photo" style="background:linear-gradient(180deg,#8fb6e0,#e8eef3 55%,#2f5fa8)" role="img" aria-label="Workers painting a building facade"></div>
  <div class="blog-body">
    <h4>House Painting</h4>
    <p>Phasellus aliquet, risus at blandit lobortis, tortor neque accumsan sem, in aliquet purus purus...</p>
    <div class="blog-meta"><span class="cat">Ink Paint</span> • 11 Mar 2016 • 1 Comment</div>
  </div>
</article>

<footer class="abs site-footer">
  <div class="abs brand footer-brand" style="left:90px;top:125px"><span class="brand-mark"></span><span class="brand-name">BRUSH HARBOR</span></div>
  <p class="abs footer-text" style="left:93px;top:195px">Lorem ipsum dolor sit amet, consectetur adipiscing elit, sed do eiusmod temporincididunt ut labore et doloremagna aliqua.</p>
  <div class="abs" style="left:95px;top:257px;display:flex;gap:32px">
    <span class="social"></span><span class="social"></span><span class="social"></span>
  </div>

  <h4 class="abs footer-head" style="left:456px;top:98px">QUICK LINKS</h4>
  <ul class="abs footer-links" style="left:468px;top:145px">
    <li>Home</li><li>About</li><li>Services</li><li>Projects</li>
  </ul>

  <h4 class="abs footer-head" style="left:692px;top:95px">CONTACT INFO</h4>
  <div class="abs" style="left:692px;top:142px">
    <div class="contact-row"><span class="dot-icon"><svg width="11" height="11" viewBox="0 0 24 24"><path fill="#fff" d="M6.6 10.8a15.1 15.1 0 0 0 6.6 6.6l2.2-2.2a1 1 0 0 1 1-.25 11.4 11.4 0 0 0 3.6.57 1 1 0 0 1 1 1V20a1 1 0 0 1-1 1A17 17 0 0 1 3 4a1 1 0 0 1 1-1h3.5a1 1 0 0 1 1 1c0 1.25.2 2.45.57 3.57a1 1 0 0 1-.25 1z"/></svg></span><div><small>CALL US</small><span>209 555 0172</span></div></div>
    <div class="contact-row"><span class="dot-icon"><svg width="11" height="11" viewBox="0 0 24 24"><rect x="3" y="6" width="18" height="12" fill="#fff"/><path d="M3 6l9 7 9-7" stroke="#c22a4d" stroke-width="2" fill="none"/></svg></span><div><small>SEND AN EMAIL</small><span>hello@brushharbor.example</span></div></div>
    <div class="contact-row"><span class="dot-icon"><svg width="11" height="11" viewBox="0 0 24 24"><path fill="#fff" d="M12 2a7 7 0 0 0-7 7c0 5 7 13 7 13s7-8 7-13a7 7 0 0 0-7-7zm0 9.5A2.5 2.5 0 1 1 12 6.5a2.5 2.5 0 0 1 0 5z"/></svg></span><div><small>LOCATION</small><span>Your Address Here</span></div></div>
  </div>

  <h4 class="abs footer-head" style="left:949px;top:95px">STAY UPDATED</h4>
  <p class="abs legal" style="left:97px;top:362px">Copyright 2024 Brush Harbor. All Rights Reserved.</p>
  <p class="abs legal" style="left:924px;top:366px">Privacy Policy | Terms &amp; Conditions</p>
</footer>
<div class="abs email-field">EMAIL ADDRESS</div>
<a class="abs btn signup">SIGNUP NOW</a>

</body>
</html>
```